Bright Path Yard Frost Maintenance

I need a logo with a roughly horizontal rectangular shape incorporating the color green and white. I want the green part to have the word green and white letters and the clean part to have the word clean in green letters
Updates

Would really appreciate a graphic grass image along bottom of design Added Wednesday, April 22, 2015

Target Market(s)

Baby Boomers who want to remain in their homes

Contact Information for Business Card

back of card will list the following details vertically;Phrase 1
Affordable Reliable Trustworthy, Phrase 2 Give yourself Freedom and Peace-of-Mind Phrase 3 Commercial Grade Equipment Phrase 4 Each Lawn neatly Cut, Trimmed and Air Blown for that Professional Touch!

Font styles to use
Other font styles liked:
• Calibri preferred

Requirements
Must have
• The word ESTIMATE and a line at bottom, back of card for easy fill in
Nice to have
• Beautiful Grass detail along bottom front of card

```html
<!DOCTYPE html>
<html lang="en">
<head>
<meta charset="utf-8">
<title>Bright Path Yard Frost Maintenance — Business Card</title>
<link rel="stylesheet" href="https://fonts.googleapis.com/css2?family=Lato:wght@400&display=swap">
<style>
  :root {
    --backdrop: #2e2e2e;
    --card-white: #f4f4f4;
    --card-grey: #dcdcdc;
    --leaf-green: #6fb23e;
    --leaf-green-light: #7dc142;
    --leaf-green-dark: #2f5f12;
    --brand-green: #5a9e2f;
    --type-white: #ffffff;
  }
  html, body {
    margin: 0;
    width: 1200px;
    height: 873px;
    overflow: hidden;
    background: var(--backdrop);
  }
  .canvas {
    position: relative;
    width: 1200px;
    height: 873px;
  }
  .business-card {
    position: absolute;
    left: 180px;
    top: 196px;
    width: 840px;
    height: 480px;
    display: block;
    box-shadow: 0 10px 30px rgba(0,0,0,0.45);
  }
  .card-name {
    font-family: "Lato", "Carlito", Calibri, sans-serif;
    font-weight: 400;
    font-size: 66px;
    letter-spacing: 1px;
  }
  .card-name--light { fill: var(--type-white); }
  .card-name--green { fill: var(--brand-green); }
</style>
</head>
<body>
<main class="canvas">
  <svg class="business-card" viewBox="0 0 840 480" xmlns="http://www.w3.org/2000/svg" aria-label="Bright Path Yard Frost Maintenance business card">
    <defs>
      <linearGradient id="paper" x1="0" y1="0" x2="1" y2="1">
        <stop offset="0" stop-color="var(--card-white)"/>
        <stop offset="1" stop-color="var(--card-grey)"/>
      </linearGradient>
      <linearGradient id="leaf" x1="0" y1="0" x2="1" y2="1">
        <stop offset="0" stop-color="var(--leaf-green-light)"/>
        <stop offset="1" stop-color="var(--leaf-green)"/>
      </linearGradient>
    </defs>

    <rect class="card-paper" width="840" height="480" fill="url(#paper)"/>

    <path class="wave-edge" fill="var(--leaf-green-dark)"
          d="M0 0 H840 V124 C700 94 560 154 420 254 C300 336 150 346 0 318 Z"/>
    <path class="wave-band" fill="url(#leaf)"
          d="M0 0 H840 V110 C700 80 560 140 420 240 C300 320 150 330 0 300 Z"/>

    <text class="card-name card-name--light" x="48" y="282">BRIGHT</text>
    <text class="card-name card-name--green" x="540" y="245">PATH</text>
  </svg>
</main>
</body>
</html>
```